Fleur Vallon Riding School Flyer Design

We need a flyer for our Horse riding school, called Fleur Vallon Riding School.

At Fleur Vallon Riding School, Horses and ponies are carefully matched to suit each rider's experience, ability and confidence. I am a Qualified instructor, equipped to train all levels from nervous beginners to the more advanced.

Horse riding is fun! Riders, particularly children, are taught not only skills on the horse, but skills that are integral to good horsemanship and ownership of horses.

We regularly host Ladies Days, Guest Instructors, 1 hour Trail Rides and Pony Ride Days!

We teach people how to interact safely with, and care for horses so they develop a genuine love and respect for the animals and the sport.

In addition to fundamental riding techniques including walk, trot, and canter, we teach our students:
Grooming and Care of horses, Safety around horses, Balance and Co-Ordination, How to saddle up and care for Tack, Responsibility for equipment and horse, Confidence and Confidence Building for all Ages.

Private and group lessons start at 5 years of age upwards.

We recommend children 4 years and under partake in 15 minute pony rides, mainly due to their attention span!

```html
<!DOCTYPE html>
<html lang="en">
<head>
<meta charset="utf-8">
<title>Fleur Vallon Riding School Flyer</title>
<link href="https://fonts.googleapis.com/css2?family=Nunito:wght@400;600;800;900&display=swap" rel="stylesheet">
<style>
  :root {
    --page: #ecebe7;
    --gold-light: #eedcb6;
    --gold: #d9bf8a;
    --gold-dark: #c7a76c;
    --ink: #141414;
    --ink-soft: #2a2a2a;
    --green: #5d7c37;
    --green-dark: #4f6c2c;
    --black: #0b0b0b;
    --white: #ffffff;
  }
  * { box-sizing: border-box; margin: 0; padding: 0; }
  html, body {
    width: 1200px; height: 1000px; overflow: hidden;
    background: var(--page);
    font-family: "Nunito", Arial, sans-serif;
  }
  .flyer {
    position: absolute; left: 100px; top: 150px;
    width: 1000px; height: 700px;
    background: var(--white);
    box-shadow: 0 6px 24px rgba(0,0,0,.18);
    overflow: hidden;
  }
  .photo-strip {
    position: absolute; left: 0; top: 0; width: 1000px; height: 300px;
    display: flex; gap: 4px; background: var(--white);
  }
  .photo { height: 100%; }
  .photo--groom {
    width: 320px;
    background: linear-gradient(135deg, #dfe3de 0%, #b9c3a6 45%, #6f7f52 100%);
  }
  .photo--arena {
    width: 320px;
    background: linear-gradient(180deg, #c6d6b7 0%, #9aa97e 40%, #b89a78 70%, #c3a585 100%);
  }
  .photo--ride {
    flex: 1;
    background: linear-gradient(180deg, #dfe7e6 0%, #89a36a 35%, #6f8f45 55%, #c4a98d 75%, #cdb196 100%);
  }
  .brand-box {
    position: absolute; left: 222px; top: 165px;
    width: 200px; height: 150px;
    background: var(--white);
    border: 8px solid var(--gold);
    display: flex; flex-direction: column; align-items: center; justify-content: center; gap: 10px;
  }
  .brand-box__mark { width: 18px; height: 18px; background: var(--ink); }
  .brand-box__name {
    font-weight: 600; font-size: 17px; letter-spacing: 2px;
    color: var(--ink); text-align: center; line-height: 1.35; text-transform: uppercase;
  }
  .age-badge {
    position: absolute; left: 560px; top: 150px;
    width: 200px; height: 150px;
    background: var(--white);
    border: 8px solid var(--green);
    border-radius: 34px;
    display: flex; flex-direction: column; align-items: center; justify-content: center;
    text-align: center; color: var(--ink);
    font-weight: 800; font-size: 16px; line-height: 1.2;
  }
  .age-badge__big { color: var(--green); font-size: 25px; font-weight: 900; margin: 2px 0; letter-spacing: -.5px; }
  .info-band {
    position: absolute; left: 0; top: 300px; width: 1000px; height: 255px;
    background: linear-gradient(180deg, var(--gold-light) 0%, var(--gold) 60%, var(--gold-dark) 100%);
    padding: 26px 40px 0;
  }
  .headline {
    font-weight: 900; font-size: 25px; line-height: 1.2; color: var(--ink);
    text-align: center; letter-spacing: -.2px;
  }
  .columns {
    display: flex; margin-top: 26px; gap: 0;
  }
  .column {
    flex: 1; font-size: 17px; line-height: 1.3; color: var(--ink-soft);
    padding: 0 18px;
  }
  .column + .column { border-left: 2px solid var(--ink-soft); }
  .column:first-child { padding-left: 0; flex: 1.15; }
  .footer-band { position: absolute; left: 0; top: 555px; width: 1000px; height: 145px; display: flex; }
  .skills {
    width: 530px; background: var(--green); color: var(--white);
    padding: 22px 30px;
  }
  .skills__title { font-weight: 800; font-size: 18px; line-height: 1.25; }
  .skills__list { font-size: 14.5px; line-height: 1.3; margin-top: 10px; }
  .pony-note {
    flex: 1; background: var(--black); color: var(--white);
    display: flex; align-items: center; padding: 0 34px;
    font-weight: 800; font-size: 21px; line-height: 1.3;
  }
</style>
</head>
<body>
  <main class="flyer">
    <section class="photo-strip">
      <div class="photo photo--groom" role="img" aria-label="Smiling girl in a riding helmet standing beside a white horse"></div>
      <div class="photo photo--arena" role="img" aria-label="Young riders on brown horses walking around a sand arena"></div>
      <div class="photo photo--ride" role="img" aria-label="Child in a red jacket riding a bay horse in a fenced paddock"></div>
    </section>

    <div class="brand-box">
      <span class="brand-box__mark"></span>
      <span class="brand-box__name">Fleur Vallon<br>Riding School</span>
    </div>

    <div class="age-badge">
      <span>Private and group<br>lessons start at</span>
      <span class="age-badge__big">5 years of age</span>
      <span>upwards</span>
    </div>

    <section class="info-band">
      <h1 class="headline">Fleur Vallon Riding School, Horses and ponies are carefully matched to suit each rider’s experience, ability and confidence. I am a Qualified instructor, equipped to train all levels from nervous beginners to the more advanced.</h1>
      <div class="columns">
        <p class="column">Horse riding is fun! Riders, particularly children, are taught not only skills on the horse, but skills that are integral to good horsemanship and ownership of horses.</p>
        <p class="column">We regularly host Ladies Days, Guest Instructors, 1 hour Trail Rides and Pony Ride Days!</p>
        <p class="column">We teach people how to interact safely with, and care for horses so they develop a genuine love and respect for the animals and the sport.</p>
      </div>
    </section>

    <section class="footer-band">
      <div class="skills">
        <h2 class="skills__title">In addition to fundamental riding techniques including walk, trot, and canter, we teach our students:</h2>
        <p class="skills__list">Grooming and Care of horses, Safety around horses, Balance and Co-Ordination, How to saddle up and care for Tack, Responsibility for equipment and horse, Confidence and Confidence Building for all Ages.</p>
      </div>
      <p class="pony-note">We recommend children 4 years and under partake in 15 minute pony rides, mainly due to their attention span!</p>
    </section>
  </main>
</body>
</html>
```